Design Only - Custom Travel Brand E-Commerce *

I have a basic website layout already made on Shopify, but looking for some additional design touches on a few pages. We would like to add some more style and creativity to the site. The images on the site are not final, just placeholders.

We are a travel brand selling our first 2 items (custom luggage tag & passport wallet). The premise is to engrave the product with everywhere you have been and everywhere you will go. You are allowed to ship back to us and re-engrave new places for $5.

The customizer page is already coded but we can make changes to the forms (select countries, enter contact information form, and overall flow)

Target Market(s)

Millennials and travelers. Most likely more females then males will be purchasing. Also for parents buying children gift cards/gifts

Industry/Entity Type

E-Commerce

Number of Pages Required

5+ page

Font styles to use
Sans Serif

Colors
85cae6
3176b5
acd136

Requirements
Must have
• Looking for ways to add some new design to the pages. It's a new product category so want the customer to fully understand what it is and how it works. The gifting page will be important because you can either buy a blank tag/passport holder as a gift ($5 paid one-time return included) or a gift card from the gifting page.
Nice to have
• Looking to add a bit of color. Gray is ok. Brand is primarily black and white but would be nice to add a TINY pop of color on certain buttons maybe.
Should not have
• The customizer feature is fixed. You can change the form look/feel.

```html
<!DOCTYPE html>
<html lang="en">
<head>
<meta charset="utf-8">
<title>Wanderlane – Home</title>
<link href="https://fonts.googleapis.com/css2?family=Oswald:wght@300;400;500;600&family=Roboto:wght@400;500;700&display=swap" rel="stylesheet">
<style>
:root{
  --lime:#acd136;
  --blue:#3176b5;
  --sky:#85cae6;
  --ink:#1c1c1c;
  --text:#3a3a3a;
  --muted:#7a7a7a;
  --line:#e2e2e2;
  --panel:#f3f3f3;
  --white:#ffffff;
  --red:#e0263a;
  --gold:#f2b01e;
}
*{box-sizing:border-box;margin:0;padding:0}
html,body{width:1200px;height:4284px;overflow:hidden}
body{font-family:"Roboto",Arial,sans-serif;color:var(--text);background:var(--white);position:relative}
.heading{font-family:"Oswald","Arial Narrow",sans-serif;color:var(--ink);text-transform:uppercase}
.btn{display:inline-flex;align-items:center;justify-content:center;font-family:"Roboto",Arial,sans-serif;font-weight:500;color:var(--white);text-transform:uppercase;letter-spacing:.5px;border:none}
.btn-blue{background:var(--blue)}
.btn-lime{background:var(--lime)}
.btn-dark{background:#3b3b3b}
.placeholder{position:absolute;display:block}

/* announcement */
.announce{position:absolute;top:0;left:0;width:1200px;height:32px;background:var(--lime);display:flex;align-items:center;justify-content:center;gap:10px;color:var(--white);font-size:13px}

/* header */
.site-header{position:absolute;top:32px;left:0;width:1200px;height:56px;border-bottom:1px solid var(--line);background:var(--white)}
.logo{position:absolute;left:112px;top:12px;height:32px;padding:0 10px;border:2px solid var(--ink);display:flex;align-items:center;font-family:"Oswald",sans-serif;font-weight:600;font-size:17px;letter-spacing:1px;color:var(--ink)}
.main-nav{position:absolute;left:404px;top:0;height:56px;display:flex;align-items:center;gap:26px;font-size:14px;color:var(--ink)}
.header-icons{position:absolute;right:112px;top:18px;display:flex;gap:16px}

/* hero */
.hero{position:absolute;top:88px;left:0;width:1200px;height:612px;overflow:hidden}
.hero-photo{left:0;top:0;width:1200px;height:612px;background:linear-gradient(90deg,#3a3532 0%,#6d625b 35%,#a89e96 60%,#d8d4d0 80%,#bdb5ad 100%)}
.hero-copy{position:absolute;left:150px;top:266px;width:500px;color:var(--white)}
.hero-copy h1{font-family:"Oswald",sans-serif;font-weight:500;font-size:42px;line-height:1.1;letter-spacing:.3px;white-space:nowrap}
.hero-copy .brand-line{font-family:"Oswald",sans-serif;font-weight:300;font-size:38px;line-height:1.1;letter-spacing:2px;margin-top:2px;padding-left:110px;white-space:nowrap}
.hero .btn{position:absolute;left:312px;top:410px;width:146px;height:42px;font-size:14px}

/* featured */
.featured{position:absolute;top:700px;left:0;width:1200px;height:592px}
.featured h2{position:absolute;top:76px;width:1200px;text-align:center;font-size:30px;font-weight:600}
.featured h2 span{font-weight:300}
.product-card{position:absolute;top:140px;width:224px}
.product-card .placeholder{position:relative;width:224px;height:248px}
.product-card h3{font-size:15px;font-weight:700;color:var(--ink);margin-top:20px}
.product-card .price{font-size:13px;color:var(--text);margin-top:6px;text-decoration:underline}
.product-card .btn{width:70px;height:30px;font-size:12px;margin-top:14px}

/* product detail */
.product-detail{position:absolute;top:1292px;left:0;width:1200px;height:480px;background:var(--panel)}
.product-gallery{left:160px;top:38px;width:440px;height:370px;background:linear-gradient(135deg,#e8e8e8 0%,#d8b75a 55%,#c79a30 100%)}
.share-icons{position:absolute;left:204px;top:408px;display:flex;gap:6px}
.share-icons span{width:26px;height:26px;border-radius:50%;background:var(--blue)}
.share-icons span:nth-child(2){background:var(--sky)}
.share-icons span:nth-child(3){background:var(--lime)}
.wish{position:absolute;left:536px;top:404px}
.product-info{position:absolute;left:664px;top:96px;width:420px}
.product-info h2{font-size:24px;font-weight:600;letter-spacing:1px}
.product-info p{font-size:13.5px;line-height:1.7;color:var(--text);margin-top:12px}
.price-row{display:flex;align-items:center;gap:12px;margin-top:14px;font-family:"Oswald",sans-serif;font-size:26px}
.price-now{color:var(--red);font-weight:500}
.price-was{color:var(--muted);text-decoration:line-through}
.stars{display:flex;gap:3px;margin-left:12px}
.swatch-label{font-size:11px;color:var(--muted);margin-top:10px;text-transform:uppercase}
.swatches{display:flex;gap:10px;margin-top:8px}
.swatches span{width:24px;height:24px;border-radius:50%;border:3px solid var(--white);box-shadow:0 0 0 1px #bbb}
.product-actions{display:flex;gap:18px;margin-top:42px}
.product-actions .btn{width:170px;height:46px;font-size:14px}

/* categories */
.categories{position:absolute;top:1772px;left:0;width:1200px;height:628px}
.category{position:absolute;top:88px;width:304px}
.category .placeholder{position:relative;width:304px;height:332px}
.category h3{font-size:18px;font-weight:700;color:var(--ink);margin-top:26px}
.category p{font-size:12.5px;line-height:1.65;margin-top:10px;color:var(--text)}

/* banner */
.promo-banner{position:absolute;top:2400px;left:0;width:1200px;height:400px;overflow:hidden}
.promo-photo{left:0;top:0;width:1200px;height:400px;background:linear-gradient(90deg,#efe8dc 0%,#d9cbb5 40%,#c8a886 70%,#8e6a47 100%)}
.promo-copy{position:absolute;left:112px;top:110px;font-size:36px;line-height:1.2;letter-spacing:.5px}
.promo-copy .lead{font-weight:600}
.promo-copy .sub{font-weight:300;font-size:34px}

/* about */
.about{position:absolute;top:2800px;left:0;width:1200px;height:552px}
.about-frame{position:absolute;left:108px;top:80px;width:120px;height:120px;border-top:8px solid var(--lime);border-left:8px solid var(--lime)}
.about-photo{left:120px;top:92px;width:476px;height:382px;background:linear-gradient(135deg,#dcdcdc 0%,#a6a6a6 50%,#cfc4b4 100%)}
.about-copy{position:absolute;left:632px;top:124px;width:450px}
.about-copy h2{font-size:44px;font-weight:500;letter-spacing:1px}
.about-copy p{font-size:12.5px;line-height:1.75;margin-top:14px}
.about-copy .btn{width:146px;height:42px;font-size:13px;margin-top:24px}

/* testimonials */
.testimonials{position:absolute;top:3352px;left:0;width:1200px;height:348px;background:var(--panel)}
.testimonial{position:absolute;top:60px;width:300px;text-align:center}
.testimonial .quote{font-family:"Oswald",sans-serif;font-size:52px;line-height:1;color:var(--lime);font-weight:600}
.testimonial p{font-size:14px;line-height:1.7;color:var(--text);margin-top:6px}
.testimonial .author{font-size:12px;color:var(--muted);margin-top:12px}

/* photo strip */
.photo-strip{position:absolute;top:3700px;left:0;width:1200px;height:300px}
.strip-1{left:0;top:0;width:400px;height:300px;background:linear-gradient(135deg,#c9ccd3,#8e8a86)}
.strip-2{left:400px;top:0;width:400px;height:300px;background:linear-gradient(135deg,#6f8f4c,#8a4b9a 60%,#b56fc2)}
.strip-3{left:800px;top:0;width:400px;height:300px;background:linear-gradient(135deg,#d6b79a,#7a3f22)}

/* footer */
.site-footer{position:absolute;top:4000px;left:0;width:1200px;height:284px;background:var(--white)}
.footer-title{position:absolute;font-size:14px;font-weight:700;color:var(--ink)}
.footer-links{position:absolute;left:112px;top:136px;display:flex;gap:28px;font-size:13px;color:var(--text)}
.newsletter{position:absolute;left:704px;top:116px;display:flex}
.newsletter .field{width:260px;height:50px;border:1px solid #cfcfcf;padding:0 14px;display:flex;align-items:center;font-size:13px;color:var(--muted)}
.newsletter .btn{width:124px;height:50px;font-size:13px}
.payments{position:absolute;left:112px;top:216px;display:flex;gap:8px}
.payments span{width:58px;height:36px;border-radius:4px;border:1px solid #cfcfcf;background:#f5f5f5}
.socials{position:absolute;left:884px;top:208px;display:flex;gap:14px}
.socials span{width:18px;height:18px;border-radius:50%;background:var(--ink)}
.copyright{position:absolute;left:884px;top:246px;font-size:11px;color:var(--muted)}
</style>
</head>
<body>

<div class="announce">
  <svg width="20" height="14" viewBox="0 0 20 14" fill="none" stroke="#fff" stroke-width="1.6"><rect x="1" y="1" width="11" height="9"/><path d="M12 4h4l3 3v3h-7"/><circle cx="5" cy="11.5" r="1.6" fill="#acd136"/><circle cx="15" cy="11.5" r="1.6" fill="#acd136"/></svg>
  <span>Free Shipping on Orders over $50</span>
</div>

<header class="site-header">
  <div class="logo">WANDERLANE</div>
  <nav class="main-nav">
    <span>Home</span><span>Shop</span><span>Gifting</span><span>About Us</span><span>Register Your Tag</span>
  </nav>
  <div class="header-icons">
    <svg width="20" height="20" viewBox="0 0 20 20" fill="none" stroke="#1c1c1c" stroke-width="1.6"><circle cx="10" cy="6.5" r="4"/><path d="M2.5 19c0-4 3.4-6.5 7.5-6.5s7.5 2.5 7.5 6.5"/></svg>
    <svg width="20" height="20" viewBox="0 0 20 20" fill="none" stroke="#1c1c1c" stroke-width="1.8"><circle cx="8.5" cy="8.5" r="6"/><path d="M13 13l5.5 5.5"/></svg>
    <svg width="20" height="20" viewBox="0 0 20 20" fill="none" stroke="#1c1c1c" stroke-width="1.6"><path d="M3 6h14l-1.3 12H4.3z"/><path d="M7 8V5a3 3 0 0 1 6 0v3"/></svg>
  </div>
</header>

<section class="hero">
  <div class="placeholder hero-photo" role="img" aria-label="Airport terminal with a striped suitcase and a grey backpack"></div>
  <div class="hero-copy">
    <h1>EVERYWHERE YOU TRAVEL...</h1>
    <div class="brand-line">WANDERLANE</div>
  </div>
  <span class="btn btn-blue">Shop Now</span>
</section>

<section class="featured">
  <h2 class="heading">Featured <span>Collection</span></h2>
  <div class="product-card" style="left:112px">
    <div class="placeholder" role="img" aria-label="Blue luggage tag on white" style="background:linear-gradient(160deg,#f2f2f2 0%,#f2f2f2 30%,#3d9be0 55%,#1e6fb8 80%,#f2f2f2 100%)"></div>
    <h3>WanderTag</h3><div class="price">$450.00</div><span class="btn btn-dark">Buy Now</span>
  </div>
  <div class="product-card" style="left:360px">
    <div class="placeholder" role="img" aria-label="Red passport wallet on white" style="background:linear-gradient(160deg,#f2f2f2 0%,#f2f2f2 25%,#c7232c 50%,#8d1419 75%,#f2f2f2 100%)"></div>
    <h3>Passport Wallet</h3><div class="price">$450.00</div><span class="btn btn-dark">Buy Now</span>
  </div>
  <div class="product-card" style="left:608px">
    <div class="placeholder" role="img" aria-label="Silver travel bottle on white" style="background:linear-gradient(90deg,#f2f2f2 0%,#f2f2f2 38%,#d3d6d9 45%,#9ea3a8 55%,#f2f2f2 62%,#f2f2f2 100%)"></div>
    <h3>Travel Bottle</h3><div class="price">$450.00</div><span class="btn btn-dark">Buy Now</span>
  </div>
  <div class="product-card" style="left:856px">
    <div class="placeholder" role="img" aria-label="Brown leather travel journal on white" style="background:linear-gradient(160deg,#f2f2f2 0%,#f2f2f2 20%,#8a5a2e 45%,#5e3a1a 75%,#f2f2f2 100%)"></div>
    <h3>Travel Journal</h3><div class="price">$450.00</div><span class="btn btn-dark">Buy Now</span>
  </div>
</section>

<section class="product-detail">
  <div class="placeholder product-gallery" role="img" aria-label="Gold luggage tag with thumbnails of tag colour options"></div>
  <div class="share-icons"><span></span><span></span><span></span></div>
  <svg class="wish" width="28" height="26" viewBox="0 0 28 26" fill="none" stroke="#9a9a9a" stroke-width="1.8"><path d="M14 24S2 16 2 8.5A6 6 0 0 1 14 6a6 6 0 0 1 12 2.5C26 16 14 24 14 24z"/></svg>
  <div class="product-info">
    <h2 class="heading">WanderPass</h2>
    <p>Everywhere you've been and everywhere you'll go, the WANDERTAG is more than just your new luggage tag</p>
    <div class="price-row">
      <span class="price-now">$25.00</span><span class="price-was">$35.00</span>
      <span class="stars">
        <svg width="16" height="16" viewBox="0 0 20 20"><path fill="#f2b01e" d="M10 1l2.8 5.8 6.2.9-4.5 4.4 1.1 6.2L10 15.4l-5.6 2.9 1.1-6.2L1 7.7l6.2-.9z"/></svg>
        <svg width="16" height="16" viewBox="0 0 20 20"><path fill="#f2b01e" d="M10 1l2.8 5.8 6.2.9-4.5 4.4 1.1 6.2L10 15.4l-5.6 2.9 1.1-6.2L1 7.7l6.2-.9z"/></svg>
        <svg width="16" height="16" viewBox="0 0 20 20"><path fill="#f2b01e" d="M10 1l2.8 5.8 6.2.9-4.5 4.4 1.1 6.2L10 15.4l-5.6 2.9 1.1-6.2L1 7.7l6.2-.9z"/></svg>
        <svg width="16" height="16" viewBox="0 0 20 20"><path fill="#f2b01e" d="M10 1l2.8 5.8 6.2.9-4.5 4.4 1.1 6.2L10 15.4l-5.6 2.9 1.1-6.2L1 7.7l6.2-.9z"/></svg>
        <svg width="16" height="16" viewBox="0 0 20 20"><path fill="#f2b01e" d="M10 1l2.8 5.8 6.2.9-4.5 4.4 1.1 6.2L10 15.4l-5.6 2.9 1.1-6.2L1 7.7l6.2-.9z"/></svg>
      </span>
    </div>
    <div class="swatch-label">Color</div>
    <div class="swatches">
      <span style="background:#d4a52f"></span><span style="background:#1c1c1c"></span><span style="background:#2f4a3c"></span>
    </div>
    <div class="product-actions">
      <span class="btn btn-blue">Customize</span><span class="btn btn-lime">Buy as Gift</span>
    </div>
  </div>
</section>

<section class="categories">
  <div class="category" style="left:108px">
    <div class="placeholder" role="img" aria-label="Lime green custom luggage tag on a bag" style="background:linear-gradient(135deg,#c7a27a 0%,#b9d94a 50%,#8a6a4a 100%)"></div>
    <h3>Custom Luggage Tag</h3>
    <p>Lorem ipsum dolor sit amet, consectetur adipiscing elit, sed do eiusmod tempor incididunt ut labore et dolore magna aliqua.</p>
  </div>
  <div class="category" style="left:452px">
    <div class="placeholder" role="img" aria-label="Passport wallet with travel documents on wood" style="background:linear-gradient(135deg,#6b4a33 0%,#8c2b2b 50%,#4a3426 100%)"></div>
    <h3>Passport Wallet</h3>
    <p>Lorem ipsum dolor sit amet, consectetur adipiscing elit, sed do eiusmod tempor incididunt ut labore et dolore magna aliqua.</p>
  </div>
  <div class="category" style="left:784px">
    <div class="placeholder" role="img" aria-label="Flat lay of travel accessories on a wooden table" style="background:linear-gradient(135deg,#7a5638 0%,#a98563 50%,#5b3e27 100%)"></div>
    <h3>Travel Accessories</h3>
    <p>Lorem ipsum dolor sit amet, consectetur adipiscing elit, sed do eiusmod tempor incididunt ut labore et dolore magna aliqua.</p>
  </div>
</section>

<section class="promo-banner">
  <div class="placeholder promo-photo" role="img" aria-label="Map, camera, wallet and hat laid out on a light wood table"></div>
  <div class="promo-copy heading">
    <div class="lead">Why choose between fashion and function?</div>
    <div class="sub">Our bags combine high-quality fabrics</div>
  </div>
</section>

<section class="about">
  <div class="about-frame"></div>
  <div class="placeholder about-photo" role="img" aria-label="Suitcase handle with an engraved luggage tag"></div>
  <div class="about-copy">
    <h2 class="heading">About Us</h2>
    <p>Lorem ipsum dolor sit amet, consectetur adipiscing elit, sed do eiusmod tempor incididunt ut labore et dolore magna aliqua. Quis ipsum suspendisse ultrices gravida. Risus commodo viverra maecenas accumsan lacus vel facilisis.</p>
    <p>Lorem ipsum dolor sit amet, consectetur adipiscing elit, sed do eiusmod tempor incididunt ut labore et dolore magna aliqua. Quis ipsum suspendisse ultrices gravida.</p>
    <span class="btn btn-blue">Learn More</span>
  </div>
</section>

<section class="testimonials">
  <div class="testimonial" style="left:90px">
    <div class="quote">&ldquo;</div>
    <p>Lorem ipsum dolor sit et, consetetur adipiscin eiusmod tempor incididunt ut labore magna aliqua. Quis ipsum suspendisse Lorem ipsum dolor sit et, consetetur adipisc</p>
    <div class="author">- John Doe</div>
  </div>
  <div class="testimonial" style="left:450px">
    <div class="quote">&ldquo;</div>
    <p>Lorem ipsum dolor sit et, consetetur adipiscin eiusmod tempor incididunt ut labore magna aliqua. Quis ipsum suspendisse Lorem ipsum dolor sit et, consetetur adipisc</p>
    <div class="author">- John Doe</div>
  </div>
  <div class="testimonial" style="left:810px">
    <div class="quote">&ldquo;</div>
    <p>Lorem ipsum dolor sit et, consetetur adipiscin eiusmod tempor incididunt ut labore magna aliqua. Quis ipsum suspendisse Lorem ipsum dolor sit et, consetetur adipisc</p>
    <div class="author">- John Doe</div>
  </div>
</section>

<section class="photo-strip">
  <div class="placeholder strip-1" role="img" aria-label="Hands holding a passport wallet"></div>
  <div class="placeholder strip-2" role="img" aria-label="Colourful suitcases on a grassy path"></div>
  <div class="placeholder strip-3" role="img" aria-label="Phone, passport and leather wallet on a desk"></div>
</section>

<footer class="site-footer">
  <div class="footer-title" style="left:112px;top:104px">Quick links</div>
  <div class="footer-links"><span>Search</span><span>Shipping and Return Policy</span><span>Terms of Service</span><span>Contact</span></div>
  <div class="footer-title" style="left:704px;top:72px">Newsletter</div>
  <div class="newsletter"><div class="field">Email Address</div><span class="btn btn-blue">Subscribe</span></div>
  <div class="payments"><span></span><span></span><span></span><span></span><span></span><span></span></div>
  <div class="socials"><span></span><span></span><span></span><span></span></div>
  <div class="copyright">© 2020 Wanderlane. All Rights Reserved</div>
</footer>

</body>
</html>
```